" A MOURALVES E TEIXEDO SOCIEDADE DE ADVOGADOS é a concretização de um ideal instituído nos idos de 2007, tempo em que os sócios fundadores ainda ocupavam os bancos da Faculdade de Direito. Sediada no Jardim Vila Aurora na cidade de Sorocaba, seu Escritório conta com modernas instalações e com uma equipe selecionada de Advogados e Colaboradores especializados. Atualmente, em decorrência de sua organização operacional e do comprometimento ético e intelectual de seus profissionais, a Sociedade vem conquistando padrões de excelência e qualidade na prestação de serviços jurídicos, se sustentando em posição de destaque no cenário na Advocacia de Sorocaba e Região. "

```html
<!DOCTYPE html>
<html lang="pt-BR">
<head>
<meta charset="UTF-8">
<title>Mouralves e Teixedo – Cartão de Visita</title>
<link rel="stylesheet" href="https://fonts.googleapis.com/css2?family=Open+Sans:wght@400;600;700&display=swap">
<style>
  :root {
    --bg: #e9eaec;
    --navy: #14294a;
    --navy-deep: #0e1f3a;
    --gold: #c9a24a;
    --gold-light: #e6cd8a;
    --gold-dark: #9c7628;
    --ink: #222a36;
    --paper: #ffffff;
  }
  * { margin: 0; padding: 0; box-sizing: border-box; }
  html, body { width: 1200px; height: 1200px; overflow: hidden; }
  body {
    background: var(--bg);
    font-family: "Open Sans", Arial, sans-serif;
    position: relative;
  }
  .card {
    position: absolute;
    left: 150px;
    width: 900px;
    height: 514px;
    overflow: hidden;
    box-shadow: 0 10px 30px rgba(0,0,0,0.18);
  }
  .card-edge {
    position: absolute;
    top: 0; right: 0;
    width: 22px; height: 100%;
    background: linear-gradient(90deg, var(--gold-dark), var(--gold-light) 45%, var(--gold) 70%, var(--gold-dark));
  }
  /* Front */
  .card-front {
    top: 60px;
    background: linear-gradient(135deg, var(--navy) 0%, var(--navy-deep) 100%);
    color: var(--paper);
  }
  .front-brand {
    position: absolute;
    top: 150px; left: 0; right: 22px;
    text-align: center;
  }
  .brand-name {
    color: var(--gold);
    font-weight: 600;
    text-transform: uppercase;
    letter-spacing: 0.06em;
  }
  .front-brand .brand-name { font-size: 40px; line-height: 1.15; }
  .front-brand .brand-sub { font-size: 19px; letter-spacing: 0.32em; margin-top: 6px; }
  .front-oab {
    margin-top: 18px;
    font-size: 15px;
    letter-spacing: 0.08em;
    color: #d9dde6;
  }
  .front-web {
    position: absolute;
    top: 370px; left: 0; right: 22px;
    text-align: center;
    font-size: 22px;
    font-weight: 600;
    letter-spacing: 0.1em;
    color: var(--paper);
  }
  /* Back */
  .card-back {
    top: 626px;
    background: linear-gradient(160deg, #ffffff 0%, #f2f3f5 100%);
    color: var(--ink);
  }
  .back-brand {
    position: absolute;
    top: 80px; left: 56px;
    width: 380px;
  }
  .back-brand .brand-name { font-size: 30px; line-height: 1.15; }
  .back-brand .brand-sub { font-size: 14px; letter-spacing: 0.3em; margin-top: 4px; }
  .contact {
    position: absolute;
    top: 60px; right: 70px;
    text-align: right;
    font-size: 19px;
    line-height: 1.4;
  }
  .contact-name { color: var(--gold); font-weight: 700; font-size: 21px; }
  .contact-label { color: var(--gold); font-weight: 700; margin-top: 26px; }
  .address {
    position: absolute;
    left: 170px; top: 392px;
    font-size: 19px;
    line-height: 1.45;
    text-align: center;
    width: 520px;
  }
</style>
</head>
<body>
  <section class="card card-front" aria-label="Frente do cartão">
    <div class="front-brand">
      <div class="brand-name">Mouralves e Teixedo</div>
      <div class="brand-name brand-sub">Sociedade de Advogados</div>
      <div class="front-oab">OAB/SP 27.604</div>
    </div>
    <div class="front-web">www.mouralvesteixedo.adv.br</div>
    <div class="card-edge"></div>
  </section>

  <section class="card card-back" aria-label="Verso do cartão">
    <div class="back-brand">
      <div class="brand-name">Mouralves e Teixedo</div>
      <div class="brand-name brand-sub">Sociedade de Advogados</div>
    </div>
    <div class="contact">
      <div class="contact-name">Rodrigo Mouralves Pacheco</div>
      <div>OAB/SP 418.236</div>
      <div class="contact-label">Telefone:</div>
      <div>+ 55 (19) 3412 7750</div>
      <div class="contact-label">Email:</div>
      <div>rodrigo@mouralvesteixedo.adv.br</div>
    </div>
    <div class="address">
      Rua Doutor Aurélio Menezes Prado, 248 | Vila Aurora<br>
      Campo Verdal/SP | CEP 13472-510
    </div>
    <div class="card-edge"></div>
  </section>
</body>
</html>
```